The design should be a multi-page, foldable flyer with the logo and the product name on the front and the web address on the back.
DoLMUO is a word play on "zebra", which the design should reflect in some way.

Target Market(s)

Schools and individual teachers

Industry/Entity Type

Product

Colors
ffffff
000000

```html
<!DOCTYPE html>
<html lang="en">
<head>
<meta charset="utf-8">
<title>DoLMUO – Trifold Flyer, Inside Spread</title>
<link href="https://fonts.googleapis.com/css2?family=Roboto+Condensed:wght@300;400&display=swap" rel="stylesheet">
<style>
  :root {
    --paper: #ffffff;
    --ink: #000000;
    --text: #1a1a1a;
    --night: #0d0d0d;
    --backdrop: #e6e6e6;
    --photo-light: #f4f4f4;
    --photo-mid: #cfcfcf;
    --photo-dark: #0b0b0b;
    --photo-low: #3a3a3a;
  }
  * { box-sizing: border-box; margin: 0; padding: 0; }
  html, body {
    width: 1200px; height: 800px; overflow: hidden;
    background: var(--backdrop);
    font-family: "Roboto Condensed", "Arial Narrow", sans-serif;
  }
  .spread {
    position: absolute; left: 90px; top: 17px;
    width: 1020px; height: 766px;
    display: flex;
  }
  .panel { position: relative; width: 340px; height: 100%; }
  .panel--left { display: flex; flex-direction: column; }
  .block { padding: 0 30px; }
  .block--light { background: var(--paper); color: var(--text); height: 372px; padding-top: 52px; }
  .block--dark { background: var(--night); color: var(--paper); flex: 1; padding-top: 86px; }
  .photo-area {
    position: absolute; left: 340px; top: 0;
    width: 680px; height: 100%;
    background:
      linear-gradient(180deg, var(--photo-light) 0%, var(--photo-light) 22%, var(--photo-mid) 40%, var(--photo-dark) 56%, var(--photo-dark) 66%, var(--photo-low) 85%, #6a6a6a 100%);
  }
  .fold { position: absolute; top: 0; width: 1px; height: 100%; background: rgba(0,0,0,0.08); }
  .fold--one { left: 340px; }
  .fold--two { left: 680px; }
  .panel--overlay { padding: 52px 28px 0; color: var(--text); }
  .module-title {
    font-weight: 400; font-size: 21px; letter-spacing: 0.5px;
    text-align: center; margin-bottom: 22px; text-transform: uppercase;
  }
  .module-copy { font-weight: 300; font-size: 13.4px; line-height: 18.2px; }
  .brand {
    position: absolute; left: 20px; top: 392px;
    display: flex; align-items: center; gap: 8px;
    color: var(--paper); font-size: 20px; font-weight: 400; letter-spacing: 1px;
  }
  .brand-dot { width: 14px; height: 14px; border-radius: 50%; background: var(--paper); }
</style>
</head>
<body>
  <main class="spread">
    <section class="panel panel--left">
      <div class="block block--light">
        <h2 class="module-title">Perform</h2>
        <p class="module-copy">The PERFORM-Module lets your students perform the tests you created. During sessions you are able to monitor what students are producing and you can also pause or stop tests for individual students – for example if you suspect that someone is cheating - or the entire class. The system also keeps track of where students are situated during tests, in order for you to be able reveal cheating attempts afterwards.</p>
      </div>
      <div class="block block--dark">
        <h2 class="module-title">Administrate</h2>
        <p class="module-copy">The ADMINISTRATE-Module contains all administrative data you need within the system. Here you can create, update and delete users, assign them different roles and rights that govern what they are and are not allowed to do and manage your subjects and classes.</p>
      </div>
    </section>

    <div class="photo-area" role="img" aria-label="Black and white photograph of open book pages fanning in from above and below against a dark background"></div>
    <div class="fold fold--one"></div>
    <div class="fold fold--two"></div>

    <section class="panel panel--overlay">
      <h2 class="module-title">Revise</h2>
      <p class="module-copy">With the REVISE-Module you can mark the tests previously performed by your students. A lot of different types of tasks can be auto-marked by the system – e.g. Multiple Choice, Short Answers, etc. – freeing you up to concentrate on marking textual work. When marking texts, you can define your own custom error types, allowing you to personalize your markings and to give students the best possible feedback.</p>
      <div class="brand"><span class="brand-dot"></span><span class="brand-name">DoLMUO</span></div>
    </section>

    <section class="panel panel--overlay">
      <h2 class="module-title">Analyze</h2>
      <p class="module-copy">The ANALYZE-Module provides several different reports and tools that help you understand the data within your system, like how student performance has changed over time in general or how they perform on specific tasks, tests or even subjects</p>
    </section>
  </main>
</body>
</html>
```